Flyer-Design für Großhändler/Onlineshop
Zielgruppe
Velorin ist ein Großhändler für Geschäftskunden. Wir liefern Artikel der Sparten Elektronik, Bürobedarf & Verpackung über unseren Business to Business-Webshop www.velorin-beispiel.de. Der Flyer richtet sich an Firmen aus der Region mit Bedarfen in den oben genannten Produktbereichen.
Aufgabenstellung
Wir benötigen einen Zickzack-Falz Flyer 6-seitig mit den Maßen 99x210mm pro Seite, passend für DIN-Lang Briefe. Des weiteren soll unser Logo auf der Startseite oben angebraucht werden. Als Farben sollen vor allem Orange, Schwarz und Weiß verwendet werden. Zusätzlich soll es für jeden Produktbereich eine Seite des Flyers geben. Soll bedeuten: Seite 1 (Normale Startseite) Seite 2 (Elektronik) Seite 3 (Bürobedarf) Seite 4 (Verpackung) Seite 5 (Onlineshop) Seite 6 (Unternehmen und Abbildung Standort wie Ortsplan Pro, unten Impressum).
Wir treten als Vertriebspartner namhafter Hersteller auf.
Binden Sie unbedingt unsere Hersteller-Logos ein.
Alle Texte finden Sie im Dateiupload.
Gerne können Sie auch Fotos unserer Webseite nehmen.
Webshop:
www.velorin-beispiel.de
Facebook:
www.sozialnetz-beispiel.de/velorin

```html
<!DOCTYPE html>
<html lang="de">
<head>
<meta charset="utf-8">
<title>Velorin – Zickzack-Flyer</title>
<link href="https://fonts.googleapis.com/css2?family=Oswald:wght@300;400;500&family=Roboto+Condensed:wght@300;400&display=swap" rel="stylesheet">
<style>
:root{
  --orange:#e8661c;
  --orange-dark:#c9501a;
  --ink:#2b2b2b;
  --text:#4a4a4a;
  --paper:#f2f2f2;
  --paper-grey:#dedede;
  --dark:#3a3a3a;
  --stage:#d4d4d4;
}
*{box-sizing:border-box;margin:0;padding:0}
html,body{width:1200px;height:600px;overflow:hidden}
body{background:var(--stage);font-family:"Roboto Condensed",sans-serif;color:var(--text)}
.strip{position:absolute;top:104px;display:flex;box-shadow:0 6px 18px rgba(0,0,0,.25)}
.strip--inside{left:30px}
.strip--outside{left:615px}
.panel{position:relative;width:185px;height:392px;background:linear-gradient(180deg,#f5f5f5,#e4e4e4);display:flex;flex-direction:column;overflow:hidden}
.panel + .panel{border-left:1px solid rgba(0,0,0,.08)}
.panel__head{height:40px;background:var(--orange);color:#fff;font-family:"Oswald",sans-serif;font-weight:300;font-size:15px;letter-spacing:2px;padding:12px 0 0 16px}
.photo{height:100px;flex:none}
.panel__body{flex:1;padding:10px 14px 0 16px;font-size:5.6px;line-height:1.45}
.panel__body p{margin-bottom:5px}
.lead{font-family:"Oswald",sans-serif;font-weight:500;color:var(--orange);font-size:7px;line-height:1.35;text-transform:uppercase;margin:4px 0 6px}
.brands{height:78px;flex:none;background:var(--paper);position:relative;display:grid;grid-template-columns:repeat(3,1fr);align-content:center;gap:10px 4px;padding:8px 8px 0;font-family:"Oswald",sans-serif;font-size:8px;font-weight:500;color:var(--ink);text-align:center}
.brands::before,.url-bar::before{content:"";position:absolute;top:-1px;left:50%;margin-left:-7px;border:7px solid transparent;border-top-color:#e6e6e6}
.call{position:absolute;right:6px;top:250px;width:58px;height:58px;border-radius:50%;background:var(--orange-dark);color:#fff;text-align:center;font-family:"Oswald",sans-serif;font-size:8.5px;line-height:1.1;padding-top:8px}
.call svg{display:block;margin:0 auto 2px}
.ticks{list-style:none;margin-top:4px}
.ticks li{position:relative;padding-left:9px;margin-bottom:4px;font-size:5.8px}
.ticks li::before{content:"";position:absolute;left:0;top:1px;width:3px;height:5px;border:solid var(--orange);border-width:0 1.4px 1.4px 0;transform:rotate(45deg)}
.shop-title{font-family:"Oswald",sans-serif;color:var(--orange);font-size:10px;line-height:1.2;margin:4px 0 6px}
.url-bar{height:78px;flex:none;background:var(--paper);position:relative;display:flex;align-items:center;justify-content:center;font-family:"Oswald",sans-serif;font-weight:300;font-size:11.5px;color:var(--ink)}
.section-bar{height:18px;background:var(--dark);color:#fff;font-family:"Oswald",sans-serif;font-weight:300;font-size:9px;letter-spacing:1.5px;padding:3px 0 0 16px;flex:none}
.map{height:100px;flex:none}
.imprint{flex:1;background:var(--paper);padding:8px 10px 0 14px;font-size:5.3px;line-height:1.45;display:flex;gap:8px}
.imprint strong{font-family:"Oswald",sans-serif;font-weight:400;font-size:7px;color:var(--ink);display:block}
.cover__logo{height:58px;background:#f4f4f4;display:flex;align-items:center;justify-content:center;font-family:"Oswald",sans-serif;font-weight:400;font-size:24px;color:var(--ink)}
.cover__claim{height:98px;background:var(--orange);color:#fff;font-family:"Oswald",sans-serif;font-weight:300;font-size:10.5px;letter-spacing:1px;line-height:2.1;padding:20px 0 0 20px}
.cover__photo{flex:1}
.cover__foot{height:42px;background:var(--dark);color:#ddd;font-family:"Oswald",sans-serif;font-weight:300;font-size:7.5px;text-align:right;padding:18px 12px 0}
</style>
</head>
<body>

<div class="strip strip--inside">
  <section class="panel">
    <h2 class="panel__head">ELEKTRONIK</h2>
    <div class="photo" role="img" aria-label="Foto: Mann telefoniert mit Smartphone in hellem Schlafzimmer" style="background:linear-gradient(135deg,#e9e6e2,#b9aea4)"></div>
    <div class="panel__body">
      <p class="lead">Mit Elektronikartikeln von Premium Marken wie Kernspeicher oder Datalux sind Sie im Bereich der Speichermedien auf der sicheren Seite.</p>
      <p>Entdecken Sie in unserem Sortiment von Micro SD über SDHC oder SDXC Flash Karten, bis zu SSD Festplatten genau die richtigen Produkte für schnelle Prozesse im Geschäftsalltag.</p>
      <p>Zusätzlich umfasst unser Portfolio der Sparte Elektronik hochwertige Ladekabel &amp; Adapter z.B. von Voltix, der etablierten Marke für Zubehör im Bereich des Mobilfunks.</p>
      <p>Elektronikartikel unterstützen Ihre Mitarbeiter und Arbeitsplätze im hektischen Alltagsgeschäft.</p>
      <p>Achten Sie auf ausreichend Schutz für Ihre mobilen Endgeräte wie Tablets oder Smartphones und verwenden Sie Schutzhüllen und Panzerfolien von Veloce, Schalenwerk und Folienhaus.</p>
    </div>
    <div class="brands"><span>Kernspeicher</span><span>Datalux</span><span>Veloce</span><span>Ramwerk</span><span>Fortana</span><span>Voltix</span></div>
  </section>

  <section class="panel">
    <h2 class="panel__head">BÜROBEDARF</h2>
    <div class="photo" role="img" aria-label="Foto: Wandregale mit Ordnern und bunten Büchern vor weißer Ziegelwand" style="background:linear-gradient(180deg,#f1f1f1,#cfcfcf)"></div>
    <div class="panel__body">
      <p>Bürobedarf gehört zu den Kernbegriffen im Geschäftsbetrieb und ist aus dem Arbeitsalltag nicht mehr wegzudenken.</p>
      <p>Bei Velorin finden Sie etablierte Marken wie Kuvero, Markant oder Papiron.</p>
      <p class="lead" style="font-size:8px">Setzen Sie auf qualitativ hochwertige Produkte ab Lager Musterhausen.</p>
      <p>Von Briefumschlägen oder Schreibwaren über Papiere, bis hin zu verschiedensten Schreibwaren-Utensilien liefern wir Ihnen Verbrauchsgüter des täglichen Bedarfs aus einer Hand.</p>
    </div>
    <div class="brands"><span>Kuvero</span><span>Markant</span><span>Ordnix</span><span>Papiron</span><span>Stempla</span><span>Tischwerk</span></div>
  </section>

  <section class="panel">
    <h2 class="panel__head">VERPACKUNG</h2>
    <div class="photo" role="img" aria-label="Foto: Lagerhalle mit Paletten und Lagerarbeiter mit Helm" style="background:linear-gradient(135deg,#c9c3b9,#8e8579)"></div>
    <div class="panel__body">
      <p>Unter den Begriff Verpackung fallen eine Vielzahl von Produkten.</p>
      <p>Vor allem für Industrie und Handel ist dieses eine Produktsparte mit vielen Berührungspunkten.</p>
      <p>Mittels des Velorin Fuhrparks liefern wir selbst größere Mengen im Umkreis von 50km termingerecht an.</p>
      <p class="lead" style="font-size:8px;width:110px">Fordern Sie jetzt unsere Service-Informationen an.</p>
    </div>
    <div class="call">
      <svg width="10" height="12" viewBox="0 0 10 12"><rect x="1.5" y="0.5" width="7" height="11" rx="1.2" fill="none" stroke="#fff" stroke-width="1"/><line x1="4" y1="9.5" x2="6" y2="9.5" stroke="#fff"/></svg>
      (01234)<br>567890
    </div>
    <div class="brands" style="grid-template-columns:repeat(2,1fr)"><span>Packfix</span><span>Klebra</span><span>Kartona</span><span>Werkfest</span></div>
  </section>
</div>

<div class="strip strip--outside">
  <section class="panel">
    <h2 class="panel__head">ONLINESHOP</h2>
    <div class="photo" role="img" aria-label="Foto: Hochregallager mit Kartons" style="background:linear-gradient(135deg,#c8ab88,#6f5d4b)"></div>
    <div class="panel__body">
      <h3 class="shop-title">Entdecken Sie unseren hochmodernen BtoB-Webshop</h3>
      <ul class="ticks">
        <li>Originalprodukte führender Hersteller</li>
        <li>Hohe Lagerverfügbarkeit für eilige Bedarfe</li>
        <li>24/7 Verfügbarkeit</li>
        <li>Integriertes Ampelsystem</li>
        <li>Individuelle Nettopreise</li>
        <li>Ansprechende Staffelpreisstruktur</li>
        <li>Suche über Bestelltext &amp; Herstellerteilenummer</li>
        <li>Sofortige Bestellbestätigung per Mail</li>
      </ul>
    </div>
    <div class="url-bar">www.velorin-beispiel.de</div>
  </section>

  <section class="panel">
    <h2 class="panel__head">UNTERNEHMEN</h2>
    <div class="panel__body" style="flex:none;height:114px;padding-top:12px">
      <p>Velorin ist Ihr Partner für Elektronik, Bürobedarf und Verpackung der Region.</p>
      <p>Als ortsansässiger Großhändler arbeiten wir mit marktführenden Herstellern zusammen.</p>
      <p>Seit der Gründung in 2014 bieten wir Produkt und Service im Einklang für Geschäftskunden.</p>
    </div>
    <div class="section-bar">STANDORT</div>
    <div class="map" role="img" aria-label="Ortsplan Pro: Standortkarte von Velorin mit Markierung" style="background:linear-gradient(135deg,#ecebe6,#d8d9cf)"></div>
    <div class="imprint">
      <div><strong>Velorin</strong>Jonas Brenner<br>Lindenweg 7<br>12345 Musterhausen<br><br>www.velorin-beispiel.de<br>www.sozialnetz-beispiel.de/velorin</div>
      <div style="padding-top:14px">Telefon: 01234-567890<br>Telefax: 01234-567891<br>E-Mail: info@velorin-beispiel.de</div>
    </div>
  </section>

  <section class="panel">
    <div class="cover__logo">Velorin</div>
    <div class="cover__claim">IHR PARTNER FÜR<br>ELEKTRONIK, BÜROBEDARF<br>UND VERPACKUNG</div>
    <div class="cover__photo" role="img" aria-label="Foto: Drei Kollegen besprechen sich am Laptop im Büro" style="background:linear-gradient(135deg,#a9a39a,#5c5650)"></div>
    <div class="cover__foot">www.velorin-beispiel.de</div>
  </section>
</div>

</body>
</html>
```